Business Card Design Project

Name: Kunle O. Edet
Designation: Partner
Address: QRM Building, 14 Harmony Close, P.O. Box 58314, Victoria Island Lagos, Nigeria
Tel: +234 1 7395162
mobile: +234 1 7061527394
Email: koedet@larkmoorassociates.com
website www.larkmoorassociates.com

```html
<!DOCTYPE html>
<html lang="en">
<head>
<meta charset="utf-8">
<title>Larkmoor Associates – Business Card</title>
<link rel="stylesheet" href="https://fonts.googleapis.com/css2?family=Arimo:wght@700&family=Open+Sans:wght@400;600&display=swap">
<style>
  :root {
    --stage: #e6e4e1;
    --card-black: #0b0b0b;
    --card-white: #ffffff;
    --card-mist: #dcdcdc;
    --band-grey: #8a8a8a;
    --band-light: #c9c9c9;
    --ink: #111111;
    --ink-soft: #5a5a5a;
    --logo-grey: #6e6e6e;
    --logo-silver: #d6d6d6;
  }
  * { box-sizing: border-box; margin: 0; padding: 0; }
  html, body { width: 1200px; height: 800px; overflow: hidden; }
  body {
    background: var(--stage);
    display: flex;
    align-items: center;
    justify-content: center;
    gap: 40px;
    font-family: "Open Sans", Arial, sans-serif;
  }
  .card {
    position: relative;
    width: 540px;
    height: 310px;
    overflow: hidden;
    box-shadow: 0 6px 18px rgba(0,0,0,.18);
  }
  /* Front */
  .card-front { background: linear-gradient(160deg, var(--card-white) 0%, var(--card-white) 45%, var(--card-mist) 100%); }
  .card-front .wave { position: absolute; inset: 0; width: 100%; height: 100%; }
  .contact {
    position: absolute;
    top: 30px;
    right: 92px;
    text-align: right;
    color: var(--ink);
  }
  .contact-name {
    font-family: "Arimo", Arial, sans-serif;
    font-weight: 700;
    font-size: 19px;
    letter-spacing: .2px;
  }
  .contact-role {
    font-size: 7px;
    letter-spacing: 1px;
    color: var(--ink-soft);
    margin-top: -1px;
  }
  .contact-lines {
    list-style: none;
    margin-top: 14px;
    font-size: 10px;
    line-height: 15px;
  }
  .contact-lines .gap { margin-top: 9px; }
  .contact-lines svg {
    width: 8px; height: 8px;
    margin-left: 4px;
    vertical-align: -1px;
    fill: var(--ink);
  }
  .brand {
    position: absolute;
    left: 38px;
    top: 150px;
    display: flex;
    align-items: center;
    gap: 12px;
  }
  .brand-square {
    width: 34px; height: 34px;
    background: var(--logo-grey);
  }
  .brand-name {
    font-weight: 600;
    font-size: 26px;
    line-height: 24px;
    color: var(--logo-grey);
  }
  .brand-name span { display: block; font-size: 14px; line-height: 18px; padding-left: 2px; }
  /* Back */
  .card-back {
    background: var(--card-black);
    display: flex;
    align-items: center;
    justify-content: center;
  }
  .back-mark {
    font-weight: 600;
    font-size: 44px;
    line-height: 44px;
    color: var(--logo-silver);
    text-align: center;
  }
  .back-mark span { display: block; font-size: 20px; line-height: 30px; letter-spacing: 2px; }
</style>
</head>
<body>

  <section class="card card-front" aria-label="Business card front">
    <svg class="wave" viewBox="0 0 540 310" preserveAspectRatio="none" aria-hidden="true">
      <defs>
        <linearGradient id="band-fill" x1="0" y1="0" x2="1" y2="0">
          <stop offset="0" stop-color="#d8d8d8"/>
          <stop offset=".6" stop-color="#a8a8a8"/>
          <stop offset="1" stop-color="#7a7a7a"/>
        </linearGradient>
      </defs>
      <path d="M0,214 C150,232 300,282 392,236 C452,206 488,70 540,34 L540,100 C500,120 460,220 400,250 C300,300 150,250 0,230 Z" fill="url(#band-fill)"/>
      <path d="M0,224 C150,244 300,292 397,245 C457,215 494,100 540,74" fill="none" stroke="#ffffff" stroke-width="2"/>
      <path d="M0,232 C150,252 300,300 402,252 C462,222 500,122 540,102 L540,310 L0,310 Z" fill="var(--card-black)"/>
    </svg>

    <div class="brand">
      <div class="brand-square"></div>
      <div class="brand-name">Larkmoor<span>Associates</span></div>
    </div>

    <div class="contact">
      <p class="contact-name">Kunle O. Edet</p>
      <p class="contact-role">PARTNER</p>
      <ul class="contact-lines">
        <li>QRM Building, 14 Harmony Close</li>
        <li>P.O. Box 58314, Victoria Island Lagos, Nigeria</li>
        <li>+234 1 7395162<svg viewBox="0 0 10 10"><path d="M2 1 L4 1 L5 3.5 L3.8 4.5 C4.4 5.8 5 6.4 5.8 6.8 L6.8 5.6 L9 6.6 L9 8.5 C9 9 8.6 9.3 8 9.2 C4.3 8.6 1.3 5.6 0.9 2 C0.8 1.4 1.2 1 2 1 Z"/></svg></li>
        <li>+234 1 7061527394<svg viewBox="0 0 10 10"><rect x="2.5" y="0.5" width="5" height="9" rx="1"/><rect x="3.3" y="1.6" width="3.4" height="5.6" fill="#fff"/></svg></li>
        <li class="gap">koedet@larkmoorassociates.com<svg viewBox="0 0 10 10"><rect x="0.5" y="2" width="9" height="6.5" rx=".6"/><path d="M1 2.5 L5 5.8 L9 2.5" fill="none" stroke="#fff" stroke-width=".9"/></svg></li>
      </ul>
    </div>
  </section>

  <section class="card card-back" aria-label="Business card back">
    <p class="back-mark">Larkmoor<span>Associates</span></p>
  </section>

</body>
</html>
```